Banner for construction site to identify developer

we need a 4 foot by 8 foot banner to hang on the fence of a residential townhome development in Phoenix, Arizona that identifies Tolvane Holdings as the company behind the development/project. Also needs to include the logo, phone number, and web address. Would like to stick with the blue colors provided in the attached logo. The blues should stay the same but the letters in the logo can change to another color if necessary. Feel free to use "Tolvane Holdings" in place of "Tolvane Holdings Group". Looking for use of colors/design to take up space so banner is not just text with a logo.

Target Market(s)

drive by traffic looking at the site

Industry/Entity Type

Real Estate

Colors
0054AA
0677BA
7BADD7
CADEEF
E8F1F8

Requirements
Must have
• company name, phone number and web address

```html
<!DOCTYPE html>
<html lang="en">
<head>
<meta charset="UTF-8">
<title>Tolvane Holdings – Development Site Banner</title>
<link href="https://fonts.googleapis.com/css2?family=Poppins:wght@500;600;700&display=swap" rel="stylesheet">
<style>
  :root {
    --page-bg: #ffffff;
    --panel-light: #f2f3f5;
    --panel-light-edge: #e6e8eb;
    --brand-ink: #3a3a3c;
    --band-blue: #1d6fa3;
    --contact-blue: #12a4db;
    --contact-blue-deep: #0f98cf;
    --accent-blue: #1aa3dc;
    --photo-sky: #62daf6;
    --photo-mid: #2f86bd;
    --photo-steel: #1f4f86;
    --white: #ffffff;
  }
  * { margin: 0; padding: 0; box-sizing: border-box; }
  html, body {
    width: 1200px; height: 1200px; overflow: hidden;
    background: var(--page-bg);
    font-family: "Poppins", sans-serif;
  }
  .banner {
    position: absolute;
    left: 107px; top: 290px;
    width: 993px; height: 496px;
    display: flex;
    box-shadow: 0 3px 6px rgba(0,0,0,0.18);
  }
  .banner__info {
    width: 610px; height: 100%;
    display: flex; flex-direction: column;
  }
  .brand {
    height: 232px;
    background: linear-gradient(100deg, var(--panel-light) 0%, var(--panel-light-edge) 60%, var(--panel-light) 100%);
    display: flex; align-items: flex-end;
    padding: 0 0 34px 34px;
    gap: 14px;
  }
  .brand__mark {
    width: 42px; height: 42px;
    background: var(--accent-blue);
    margin-bottom: 10px;
  }
  .brand__name {
    font-weight: 700;
    font-size: 55px;
    line-height: 1;
    color: var(--brand-ink);
    letter-spacing: -0.5px;
  }
  .title-band {
    height: 65px;
    background: var(--band-blue);
    display: flex; align-items: center;
    padding-left: 39px;
  }
  .title-band__text {
    color: var(--white);
    font-weight: 700;
    font-size: 42px;
    letter-spacing: 5px;
    line-height: 1;
  }
  .contact {
    flex: 1;
    background: linear-gradient(180deg, var(--contact-blue-deep) 0%, var(--contact-blue) 100%);
    padding: 22px 0 0 40px;
    color: var(--white);
  }
  .contact__item { margin-bottom: 12px; }
  .contact__label {
    font-weight: 700; font-size: 24px; letter-spacing: 2px; line-height: 1.25;
  }
  .contact__value {
    font-weight: 500; font-size: 23px; letter-spacing: 2.5px; line-height: 1.35;
  }
  .contact__value--web { font-size: 20px; letter-spacing: 2px; }
  .banner__photo {
    flex: 1; height: 100%;
    background: linear-gradient(165deg, var(--photo-sky) 0%, var(--photo-mid) 50%, var(--photo-steel) 100%);
  }
</style>
</head>
<body>
  <div class="banner">
    <section class="banner__info">
      <header class="brand">
        <span class="brand__mark"></span>
        <span class="brand__name">Tolvane Holdings</span>
      </header>
      <div class="title-band">
        <h1 class="title-band__text">DEVELOPMENT SITE</h1>
      </div>
      <div class="contact">
        <div class="contact__item">
          <div class="contact__label">PHONE:</div>
          <div class="contact__value">(602) 555-0148</div>
        </div>
        <div class="contact__item">
          <div class="contact__label">WEB:</div>
          <div class="contact__value contact__value--web">WWW.TOLVANEHOLDINGSGROUP.COM</div>
        </div>
      </div>
    </section>
    <div class="banner__photo" role="img" aria-label="Photo: construction worker in hard hat and high-visibility vest tying rebar columns on site"></div>
  </div>
</body>
</html>
```